Flyer Handout when attending Dental Conventions, or dental office shows

take the sample file folder that is shown with 2 pictures. The outside and inside of the folder needs to be completed, along with the inserts. This folder pictures are from someone elses flyer/folder and i would like to have it layout like this. The KRV inserts is informational, but it is lacking originality, pictures, etc. Try to make our information and move it to 2017. When this is done, i would like to take this flyer and load it to the web or allow to send via email and make it interactive. The user can select the flyers and it will slide or flip to the flyer. this will make if kewl/fun

Target Market(s)

Dental Offices

Industry/Entity Type

Dental

Font styles to use
Serif
Sans Serif

Colors

Designer to choose colors to be used in the design.

Requirements
Must have
• a Semi new look and feel of our flyers, and a new envelope created

```html
<!DOCTYPE html>
<html lang="en">
<head>
<meta charset="utf-8">
<title>KRV Flyer – Front and Back</title>
<link rel="stylesheet" href="https://fonts.googleapis.com/css2?family=Montserrat:wght@400;500;600;700&display=swap">
<style>
  :root {
    --board: #1e1d22;
    --blue: #1a6ea1;
    --blue-deep: #14608f;
    --orange: #f49a35;
    --ink: #2b2b2b;
    --white: #ffffff;
    --photo-skin: #d9c3b4;
    --photo-cool: #e3e7ea;
    --photo-room: #c9d6df;
  }
  * { box-sizing: border-box; margin: 0; padding: 0; }
  html, body { width: 1200px; height: 1200px; overflow: hidden; }
  body {
    background: var(--board);
    font-family: "Montserrat", sans-serif;
    position: relative;
  }
  .side-label {
    position: absolute;
    top: 132px;
    color: var(--white);
    font-weight: 700;
    font-size: 44px;
  }
  .side-label--front { left: 40px; }
  .side-label--back { left: 602px; }

  .page {
    position: absolute;
    top: 210px;
    height: 780px;
    background: var(--white);
    overflow: hidden;
  }
  .page--front { left: 42px; width: 552px; }
  .page--back { left: 594px; width: 554px; }

  /* Front */
  .front-art { position: absolute; left: 0; top: 0; width: 552px; height: 600px; }
  .brand-name {
    position: absolute;
    left: 76px; top: 20px;
    color: var(--blue);
    font-weight: 700;
    font-size: 36px;
    line-height: 44px;
    letter-spacing: 1px;
    display: flex; align-items: center; gap: 8px;
  }
  .brand-dot { width: 14px; height: 14px; border-radius: 50%; background: var(--orange); }
  .headline {
    position: absolute;
    left: 0; top: 500px; width: 440px;
    text-align: center;
    color: var(--white);
    font-weight: 500;
    font-size: 23px;
    line-height: 34px;
  }
  .how {
    position: absolute;
    left: 26px; top: 610px; right: 24px;
  }
  .how h2 { color: var(--orange); font-size: 20px; font-weight: 600; margin-bottom: 6px; }
  .how p { color: var(--ink); font-size: 14.5px; line-height: 20px; }
  .footer-band {
    position: absolute;
    left: 0; bottom: 0; width: 100%;
    background: var(--orange);
    color: var(--white);
    font-weight: 600;
    text-align: center;
  }
  .page--front .footer-band { height: 62px; line-height: 62px; font-size: 14px; }

  /* Back */
  .aging {
    position: absolute; left: 0; top: 0; width: 100%; height: 292px;
    background: var(--blue);
    padding: 24px 20px 0 26px;
  }
  .aging h2 { color: var(--orange); font-size: 20px; font-weight: 700; margin-bottom: 12px; }
  .aging p { color: var(--white); font-size: 9.6px; line-height: 12.6px; margin-bottom: 11px; }
  .clinic-photo {
    position: absolute; left: 2px; top: 312px; width: 232px; height: 202px;
    background: linear-gradient(160deg, #eef2f5 0%, var(--photo-room) 55%, #8fa7bd 100%);
  }
  .features { position: absolute; left: 252px; top: 314px; right: 18px; }
  .features h2 { color: var(--orange); font-size: 20px; font-weight: 700; margin-bottom: 8px; }
  .features ul { list-style: none; }
  .features li {
    display: flex; gap: 7px;
    color: var(--ink); font-size: 10px; line-height: 12px;
    margin-bottom: 12px;
  }
  .features svg { flex: none; margin-top: 1px; }
  .contact-band { height: 248px; }
  .logo-box {
    position: absolute; left: 190px; top: 24px; width: 190px; height: 92px;
    background: var(--white);
    display: flex; align-items: center; justify-content: center; gap: 8px;
    color: var(--blue); font-weight: 700; font-size: 38px; letter-spacing: 1px;
  }
  .contact-lines { position: absolute; left: 0; top: 148px; width: 100%; font-size: 13.5px; line-height: 25px; }
</style>
</head>
<body>
  <div class="side-label side-label--front">Front</div>
  <div class="side-label side-label--back">Back</div>

  <section class="page page--front">
    <svg class="front-art" viewBox="0 0 552 600">
      <defs>
        <linearGradient id="toothTone" x1="0" y1="0" x2="1" y2="1">
          <stop offset="0" stop-color="#f4f5f6"/>
          <stop offset="1" stop-color="#e3e7ea"/>
        </linearGradient>
        <linearGradient id="childTone" x1="0" y1="0" x2="1" y2="1">
          <stop offset="0" stop-color="#c9a995"/>
          <stop offset="0.5" stop-color="#d9c3b4"/>
          <stop offset="1" stop-color="#eef0f2"/>
        </linearGradient>
      </defs>
      <rect x="0" y="0" width="552" height="600" fill="url(#toothTone)" role="img" aria-label="Photo of a large white model tooth beside a dental mirror"/>
      <polygon points="0,0 300,0 200,170 420,460 0,460" fill="url(#childTone)" role="img" aria-label="Photo of a smiling child in a dental chair during a check-up"/>
      <polyline points="300,0 200,170 420,460" fill="none" stroke="#ffffff" stroke-width="5"/>
      <polygon points="0,0 300,0 0,250" fill="#ffffff"/>
      <line x1="300" y1="0" x2="0" y2="250" stroke="#1a6ea1" stroke-width="4"/>
      <polygon points="0,462 420,462 552,600 0,600" fill="#1a6ea1"/>
      <line x1="420" y1="462" x2="552" y2="600" stroke="#ffffff" stroke-width="4"/>
    </svg>
    <div class="brand-name"><span class="brand-dot"></span>KRV</div>
    <h1 class="headline">Briging the Gap Between<br>payers and Providers</h1>
    <div class="how">
      <h2>How it Works:</h2>
      <p>Within KRV Bridge, select the NEW Eligibility Tab, Hit send and you will begin receiving all of your eligibility responses within the KRV Portal. It is that easy!</p>
    </div>
    <div class="footer-band">Call us Today at (800) 555-0147</div>
  </section>

  <section class="page page--back">
    <div class="aging">
      <h2>KRV Accounts Receivable Aging:</h2>
      <p>Are you spending too much time on the phone with insurance companies trying to figure out why your claims are not paid? KRV has a wonderful AR Aging integration that will reduce your time on the phone by 50 – 75%.</p>
      <p>Currently your office goes into your dental software and creates a report for all of your outstanding insurance claims and then prints the report to paper. It is sorted by insurance company and starting with Harbor Mutual. The insurance person would call on the first claim, Jane Porter, who has Harbor Mutual. Go through all the prompts and now wait on hold until they get a customer service rep. And now come to find out that the patient didn't have coverage, or they never received the claim, or whatever else is wrong.</p>
      <p>KRV has streamlined this process. We are able to reconcile the outstanding Insurance claims from your Dental Software to our clearinghouse and can tell what has been Paid, Rejected, and or Processed. It saves about 50 - 75% of time being spent on the phone. What is also nice about this service is that this is Web Based, and users can be at home, in the office at another computer and or be on vacation and still have access to their outstanding claims.</p>
    </div>

    <div class="clinic-photo" role="img" aria-label="Photo of a bright modern dental treatment room with a blue patient chair"></div>

    <div class="features">
      <h2>Features/Benefits:</h2>
      <ul>
        <li><svg width="10" height="10" viewBox="0 0 10 10"><path d="M1 5.5 L4 8.5 L9 1.5" fill="none" stroke="#f49a35" stroke-width="1.8"/></svg>Online Tracking of your claims</li>
        <li><svg width="10" height="10" viewBox="0 0 10 10"><path d="M1 5.5 L4 8.5 L9 1.5" fill="none" stroke="#f49a35" stroke-width="1.8"/></svg>Easy 1 click to check the status of your claims</li>
        <li><svg width="10" height="10" viewBox="0 0 10 10"><path d="M1 5.5 L4 8.5 L9 1.5" fill="none" stroke="#f49a35" stroke-width="1.8"/></svg>Ability to correct and resubmit or just resubmit your claims</li>
        <li><svg width="10" height="10" viewBox="0 0 10 10"><path d="M1 5.5 L4 8.5 L9 1.5" fill="none" stroke="#f49a35" stroke-width="1.8"/></svg>Options to track your claim results and enter notes into the claim</li>
        <li><svg width="10" height="10" viewBox="0 0 10 10"><path d="M1 5.5 L4 8.5 L9 1.5" fill="none" stroke="#f49a35" stroke-width="1.8"/></svg>Easy integration</li>
        <li><svg width="10" height="10" viewBox="0 0 10 10"><path d="M1 5.5 L4 8.5 L9 1.5" fill="none" stroke="#f49a35" stroke-width="1.8"/></svg>Eliminates time being spent on the phone with insurance companies</li>
      </ul>
    </div>

    <div class="footer-band contact-band">
      <div class="logo-box"><span class="brand-dot"></span>KRV</div>
      <div class="contact-lines">
        <p>Call us Today at (800) 555-0147</p>
        <p>Email: statements@krvdental.com</p>
        <p>www.krvdental.com</p>
      </div>
    </div>
  </section>
</body>
</html>
```